New Flyer Design Project - for sale units at The Lodge phase 3

on attached the A2 is full kitchen 1 bedroom, the A3 is gally kitchen and the B2 is the the 2 bedroom, on attached pictures the room with 2 queen beds is only for the 2 bedroom

This is going to be used to sale the units (real estate sale) so the layout could possibly be text and then pictures maybe 1 bedroom on one side and 2 on the back?

Experience the Modern Luxury of the New Phase 3 Building of the
Lodge at Harrow Bend

* Opening Spring 2019

* America's #17 Family Resort; Tennessee's Only Ranked Resort

1 Bedroom Bunk Suite (Galley Kitchen) - $199,000; Sleeps 6

* Private King Master Bedroom

* Bunk Bed Galley

* Granite Counters Throughout

* Fully Furnished with Custom Furnishings

* Private Balcony

* Equipped Galley Kitchen

* In Unit Laundry

* Queen Sleeper Sofa

1 Bedroom Bunk Suite (Full Kitchen) - $209,000; Sleeps 6

* Bunk Bed Galley

* Granite Counters throughout

* Equipped Full Kitchen

* Completely Furnished with Custom Furnishings

* Private Balcony

* In Unit Laundry

* Queen Sleeper Sofa

2 Bedroom Bunk Suite (Full Kitchen) - $249,000; Sleeps 10

* Private King Master Bedroom with On-Suite Bathroom

* Two Queen Bedroom

* Bunk Bed Galley

* Full Kitchen

* Private Balcony

* In Unit Laundry

* Queen Sleeper Sofa

Target Market(s)

people wanting to buy units in phase 3 of The Lodge at Harrow Bend

Industry/Entity Type

Real Estate Development

Requirements
Must have
• attached text to describe units and price
• pictures and layouts
• Contact Dale Porter
• 865-391-7702 Dale@bramblecrestlodges.example
Nice to have
• brand and logo
Should not have
• it should not be plain this is m ore of a luxury project

```html
<!DOCTYPE html>
<html lang="en">
<head>
<meta charset="utf-8">
<title>The Lodge at Harrow Bend – Phase 3 Flyers</title>
<link href="https://fonts.googleapis.com/css2?family=Pacifico&family=Roboto:ital,wght@0,400;0,500;0,700;0,900;1,500&display=swap" rel="stylesheet">
<style>
  :root{
    --page-bg:#d9d6d2;
    --brown-dark:#4a3a2d;
    --brown:#5e4a3a;
    --brown-light:#6e5846;
    --teal:#4d7882;
    --gold:#eaa34c;
    --white:#ffffff;
    --cream:#f3ece2;
  }
  *{box-sizing:border-box;margin:0;padding:0}
  html,body{width:1200px;height:1000px;overflow:hidden}
  body{background:var(--page-bg);font-family:"Roboto",Arial,sans-serif;position:relative}

  .flyer{
    position:absolute;top:100px;width:560px;height:800px;
    background:linear-gradient(160deg,var(--brown-light) 0%,var(--brown) 45%,var(--brown-dark) 100%);
    box-shadow:0 6px 18px rgba(0,0,0,.25);
    color:var(--white);
  }
  .flyer--one-bed{left:25px}
  .flyer--range{left:615px}

  .brand{
    position:absolute;left:24px;top:52px;width:190px;
    display:flex;align-items:center;gap:10px;
  }
  .brand__dot{width:16px;height:16px;border-radius:50%;background:var(--gold);flex:none}
  .brand__name{font-weight:700;font-size:21px;line-height:1.15;color:var(--gold)}

  .opening{position:absolute;left:230px;right:20px;top:14px;text-align:center}
  .opening__script{font-family:"Pacifico",cursive;font-size:58px;line-height:1.25;color:var(--white)}
  .opening__season{font-weight:900;font-size:32px;color:var(--gold);letter-spacing:.5px;margin-top:2px}

  .ranking{position:absolute;left:0;right:0;top:178px;text-align:center}
  .ranking__title{font-weight:700;font-size:28px;color:var(--white)}
  .ranking__sub{font-style:italic;font-weight:500;font-size:21px;color:var(--gold);margin-top:4px}

  .photos{position:absolute;left:20px;right:20px;top:268px;height:262px;display:flex;gap:10px}
  .photo{flex:1;border:3px solid var(--cream)}
  .photo--bedroom{background:linear-gradient(180deg,#c9cfa4 0%,#e8e4d8 55%,#6f7a78 100%)}
  .photo--kitchen{background:linear-gradient(180deg,#d8d2bf 0%,#b9b39c 50%,#5d6864 100%)}

  .unit{position:absolute;background:var(--teal);padding:12px 14px}
  .unit__name{font-size:13.5px;font-weight:400}
  .unit__price{font-size:17px;font-weight:700;color:var(--gold);margin:3px 0 8px}
  .unit__features{list-style:none}
  .unit__features li{position:relative;padding-left:15px;font-size:12.5px;font-weight:500;line-height:1.35}
  .unit__features li::before{content:"";position:absolute;left:0;top:5px;width:6px;height:6px;background:var(--gold)}

  .flyer--one-bed .unit{left:20px;top:548px;width:290px;height:230px}
  .floorplan{position:absolute;left:330px;top:548px;width:210px;height:135px;border:3px solid var(--cream);
    background:linear-gradient(135deg,#efe9dc,#d9cdb6)}
  .contact{position:absolute;left:318px;right:10px;top:695px;text-align:center}
  .contact__label{font-size:19px;font-weight:400}
  .contact__name{font-weight:700;color:var(--gold)}
  .contact__phone{font-size:20px;font-weight:700;color:var(--gold);margin-top:3px}
  .contact__email{font-size:11.5px;margin-top:8px}

  .flyer--range .photos{top:262px;height:226px}
  .flyer--range .unit{top:498px;width:255px;height:244px;padding:10px 12px}
  .flyer--range .unit--two-bed{left:20px}
  .flyer--range .unit--one-full{left:285px}
  .flyer--range .unit__price{margin:2px 0 6px}
  .flyer--range .unit__features li{font-size:12px;line-height:1.25}
  .flyer--range .unit__features li::before{top:4px}

  .contact-bar{position:absolute;left:40px;right:40px;top:752px;height:36px;border:2px solid var(--gold);
    border-radius:10px;display:flex;align-items:center;justify-content:center;gap:22px;font-size:18px}
  .contact-bar .contact__label{font-size:18px}
  .contact-bar .contact__phone{margin:0;font-size:18px}
</style>
</head>
<body>

<article class="flyer flyer--one-bed">
  <div class="brand"><span class="brand__dot"></span><span class="brand__name">The Lodge at Harrow Bend</span></div>
  <header class="opening">
    <div class="opening__script">Opening</div>
    <div class="opening__season">SPRING 2019</div>
  </header>
  <div class="ranking">
    <div class="ranking__title">America's #17 Family Resort</div>
    <div class="ranking__sub">Tennessee's Only Ranked Resort</div>
  </div>
  <div class="photos">
    <div class="photo photo--bedroom" role="img" aria-label="Photo of king master bedroom"></div>
    <div class="photo photo--kitchen" role="img" aria-label="Photo of galley kitchen and dining area"></div>
  </div>
  <section class="unit">
    <div class="unit__name">1 Bedroom Bunk Suite (Galley Kitchen)</div>
    <div class="unit__price">$199,000 | SLEEPS 6</div>
    <ul class="unit__features">
      <li>Private King Master Bedroom</li>
      <li>Bunk Bed Galley</li>
      <li>Granite Counters Throughout</li>
      <li>Fully Furnished with Custom Furnishings</li>
      <li>Private Balcony</li>
      <li>Equipped Galley Kitchen</li>
      <li>In Unit Laundry</li>
      <li>Queen Sleeper Sofa</li>
    </ul>
  </section>
  <div class="floorplan" role="img" aria-label="Floor plan of the 1 bedroom galley kitchen suite"></div>
  <div class="contact">
    <div class="contact__label">Contact <span class="contact__name">Dale Porter</span></div>
    <div class="contact__phone">865-391-7702</div>
    <div class="contact__email">dale@bramblecrestlodges.example</div>
  </div>
</article>

<article class="flyer flyer--range">
  <div class="brand"><span class="brand__dot"></span><span class="brand__name">The Lodge at Harrow Bend</span></div>
  <header class="opening">
    <div class="opening__script">Opening</div>
    <div class="opening__season">SPRING 2019</div>
  </header>
  <div class="ranking">
    <div class="ranking__title">America's #17 Family Resort</div>
    <div class="ranking__sub">Tennessee's Only Ranked Resort</div>
  </div>
  <div class="photos">
    <div class="photo photo--bedroom" role="img" aria-label="Photo of two queen bedroom"></div>
    <div class="photo photo--kitchen" role="img" aria-label="Photo of full kitchen and dining area"></div>
  </div>
  <section class="unit unit--two-bed">
    <div class="unit__name">2 Bedroom Bunk Suite (Full Kitchen)</div>
    <div class="unit__price">$249,000 | SLEEPS 10</div>
    <ul class="unit__features">
      <li>Private King Master Bedroom with On-Suite Bathroom</li>
      <li>Two Queen Bedroom</li>
      <li>Bunk Bed Galley</li>
      <li>Granite Counters Throughout</li>
      <li>Full Kitchen</li>
      <li>Completely Furnished with Custom Furnishings</li>
      <li>Private Balcony</li>
      <li>In Unit Laundry</li>
      <li>Queen Sleeper Sofa</li>
    </ul>
  </section>
  <section class="unit unit--one-full">
    <div class="unit__name">1 Bedroom Bunk Suite (Full Kitchen)</div>
    <div class="unit__price">$209,000 | SLEEPS 6</div>
    <ul class="unit__features">
      <li>Private King Master Bedroom</li>
      <li>Bunk Bed Galley</li>
      <li>Granite Counters throughout</li>
      <li>Equipped Full Kitchen</li>
      <li>Completely Furnished with Custom Furnishings</li>
      <li>Private Balcony</li>
      <li>In Unit Laundry</li>
      <li>Queen Sleeper Sofa</li>
    </ul>
  </section>
  <div class="contact-bar">
    <span class="contact__label">Contact <span class="contact__name">Dale Porter</span></span>
    <span class="contact__phone">865-391-7702</span>
  </div>
</article>

</body>
</html>
```